Business Card Design

Business card design.

Business card is to have logo, website address and email address.

Website is www.brightkettle.ie
Email is info@brightkettle.ie

I have ordered Business Card Printing via Print Harbor, the Double-sided colour printed option with gloss finish.

Industry/Entity Type

Business

```html
<!DOCTYPE html>
<html lang="en">
<head>
<meta charset="utf-8">
<title>Bright Kettle business card</title>
<link href="https://fonts.googleapis.com/css2?family=Nunito:wght@800&family=Arimo&display=swap" rel="stylesheet">
<style>
  :root {
    --backdrop: #c98d5c;
    --card-front: #ececec;
    --card-back: #e6e6e6;
    --card-edge: #5a5a5a;
    --swoosh: #9e9e9e;
    --brand-red: #d00d10;
    --ink: #111111;
    --text: #222222;
  }
  html, body {
    margin: 0;
    padding: 0;
    width: 1200px;
    height: 988px;
    overflow: hidden;
    background: var(--backdrop);
  }
  .canvas {
    position: relative;
    width: 1200px;
    height: 988px;
  }
  .card {
    position: absolute;
    width: 776px;
    height: 442px;
    border: 1px solid var(--card-edge);
    box-sizing: border-box;
    overflow: hidden;
  }
  .card--front { left: 45px; top: 35px; background: var(--card-front); }
  .card--back  { left: 378px; top: 501px; background: var(--card-back); }

  .brand {
    position: absolute;
    left: 0;
    width: 100%;
    text-align: center;
  }
  .brand__dot {
    display: block;
    margin: 0 auto 14px;
    width: 74px;
    height: 74px;
    border-radius: 50%;
    background: var(--brand-red);
  }
  .brand__name {
    font-family: "Nunito", sans-serif;
    font-weight: 800;
    font-size: 56px;
    line-height: 1;
    letter-spacing: 1px;
    color: var(--ink);
  }
  .card--front .brand { top: 46px; }
  .card--back .brand  { top: 128px; }

  .swoosh {
    position: absolute;
    left: 0;
    top: 0;
  }
  .contact {
    position: absolute;
    left: 0;
    top: 289px;
    width: 100%;
    text-align: center;
    font-family: "Arimo", sans-serif;
    font-size: 25px;
    letter-spacing: 1px;
    color: var(--text);
  }
  .contact__icon {
    display: inline-block;
    vertical-align: -1px;
    margin-right: 8px;
  }
</style>
</head>
<body>
<main class="canvas">
  <section class="card card--front" aria-label="Card front">
    <div class="brand">
      <span class="brand__dot"></span>
      <div class="brand__name">BRIGHTKETTLE.IE</div>
    </div>
    <svg class="swoosh" width="776" height="442" viewBox="0 0 776 442" aria-hidden="true">
      <path d="M0 233 Q388 596 776 243 L776 250 Q388 512 0 236 Z" fill="var(--swoosh)"/>
    </svg>
    <div class="contact">
      <svg class="contact__icon" width="22" height="17" viewBox="0 0 22 17" aria-hidden="true">
        <rect x="0" y="3" width="22" height="14" fill="var(--brand-red)"/>
        <path d="M0 3 L11 11 L22 3" fill="none" stroke="#ffffff" stroke-width="1.5"/>
      </svg><span class="contact__email">info@brightkettle.ie</span>
    </div>
  </section>

  <section class="card card--back" aria-label="Card back">
    <div class="brand">
      <span class="brand__dot"></span>
      <div class="brand__name">BRIGHTKETTLE.IE</div>
    </div>
  </section>
</main>
</body>
</html>
```